Want to fly? Flight school needs a roll up

Hello designers

We are a small aviation club with around 100 members. We love flying and therefore offer free flight lessons for young people at our glider flight school.
The young people only have to pay a flat rate of €300 for the aircraft until their first solo flight.
To advertise the flight school we now need a roll up banner measuring 85cm x 200cm. You can find the data sheet for the banner in the appendix.
Content of the roll up banner:
Advertising for our flight school so that we can attract new members
The banner should be designed in our club colors blue/white
The banner is aimed at all people who want to get a glider license
A great offer for young people up to the age of 25 should be placed on the banner with a reference to the text “Offer only applies to people up to the age of 25. Included in the flat rate of €300 is training on the glider up to the first "solo flight"
The banner is intended to advertise training with a glider. Therefore the wish would be for a glider to be depicted

Here is a link to our current homepage

https://www.lsg-kornbach.de/

https://www.videohub-example.com/watch?v=Q8-t2Lp4xZn

Target Market(s)

Young people from 14 years to 30 years

Colors
0054AA
0677BA
7BADD7
CADEEF
E8F1F8

Requirements
Nice to have
• Glider / club logo
Should not have
• Too much text

```html
<!DOCTYPE html>
<html lang="en">
<head>
<meta charset="utf-8">
<title>Glider Flight School – Roll-up Banner</title>
<link href="https://fonts.googleapis.com/css2?family=Roboto+Condensed:wght@700&display=swap" rel="stylesheet">
<style>
  :root {
    --stage: #e9ebf0;
    --club-blue: #1f2fb8;
    --club-blue-deep: #15208f;
    --club-blue-light: #4b5ee0;
    --badge-blue: #0b3ad0;
    --accent-magenta: #b8175e;
    --panel-white: #ffffff;
    --panel-shade: #dfe3f6;
    --text-blue: #1232c8;
    --sky-top: #f4f6fd;
    --sky-mid: #c9d2ee;
    --sky-low: #eef1fb;
  }
  * { box-sizing: border-box; margin: 0; padding: 0; }
  html, body { width: 1200px; height: 720px; overflow: hidden; }
  body {
    background: var(--stage);
    font-family: "Roboto Condensed", "Arial Narrow", sans-serif;
    position: relative;
  }
  .rollup {
    position: absolute;
    left: 456px; top: 20px;
    width: 289px; height: 680px;
    background: var(--club-blue);
    overflow: hidden;
    box-shadow: 0 10px 30px rgba(20, 30, 90, 0.25);
  }
  .rollup__header {
    position: absolute; inset: 0 0 auto 0; height: 180px;
  }
  .panel {
    position: absolute; left: 0; right: 0;
    background: linear-gradient(180deg, var(--panel-shade) 0%, var(--panel-white) 28%, var(--panel-white) 100%);
  }
  .panel--offer {
    top: 139px; height: 190px;
    border-radius: 0 22px 22px 0;
    box-shadow: 0 4px 8px rgba(30, 40, 140, 0.25);
  }
  .panel--price {
    top: 322px; height: 330px;
    border-radius: 22px 0 0 0;
  }
  .club-mark {
    position: absolute; left: 50%; top: 56px;
    width: 132px; height: 132px; margin-left: -66px;
    border-radius: 50%;
    background: radial-gradient(circle at 40% 40%, var(--club-blue-light), var(--club-blue-deep));
    border: 3px solid var(--panel-white);
    box-shadow: 0 3px 8px rgba(20, 30, 100, 0.35);
    display: flex; align-items: center; justify-content: center;
    text-align: center;
  }
  .club-mark__name {
    color: var(--panel-white);
    font-size: 14px; line-height: 1.2;
    width: 96px;
  }
  .message {
    position: absolute; left: 0; right: 0;
    text-align: center;
    color: var(--text-blue);
    font-size: 17px; line-height: 26px;
    text-transform: uppercase;
  }
  .message--offer { top: 221px; }
  .message--price { top: 384px; }
  .tag {
    display: inline-block;
    color: var(--panel-white);
    background: var(--badge-blue);
    border-radius: 4px;
    padding: 0 4px;
    line-height: 22px;
  }
  .tag--highlight { background: var(--accent-magenta); padding: 0 6px; }
  .sky-photo {
    position: absolute; left: 0; right: 0; top: 488px; height: 160px;
    background: linear-gradient(180deg, var(--sky-top) 0%, var(--sky-mid) 55%, var(--sky-low) 100%);
  }
  .rollup__footer {
    position: absolute; left: 0; right: 0; bottom: 0; height: 44px;
  }
</style>
</head>
<body>
  <main class="rollup">
    <svg class="rollup__header" viewBox="0 0 289 180" aria-hidden="true">
      <defs>
        <linearGradient id="header-fill" x1="0" y1="0" x2="1" y2="1">
          <stop offset="0" stop-color="#2a3ad0"/>
          <stop offset="1" stop-color="#1a259c"/>
        </linearGradient>
      </defs>
      <rect width="289" height="180" fill="url(#header-fill)"/>
      <circle cx="40" cy="20" r="70" fill="#ffffff" opacity="0.07"/>
      <circle cx="250" cy="60" r="80" fill="#ffffff" opacity="0.06"/>
      <circle cx="150" cy="-10" r="60" fill="#ffffff" opacity="0.05"/>
    </svg>

    <section class="panel panel--offer"></section>
    <section class="panel panel--price"></section>

    <div class="club-mark">
      <span class="club-mark__name">Luftsportgruppe Kornbach e.V.</span>
    </div>

    <p class="message message--offer">
      <span class="tag">Offer</span> is valid<br>
      only for persons<br>
      under <span class="tag">25</span> years of age.
    </p>

    <p class="message message--price">
      The price of <span class="tag">€300</span><br>
      includes training<br>
      on the glider before<br>
      the first <span class="tag tag--highlight">Solo Flight</span>
    </p>

    <div class="sky-photo" role="img" aria-label="Photo of a blue aerobatic aircraft flying above white clouds"></div>

    <svg class="rollup__footer" viewBox="0 0 289 44" preserveAspectRatio="none" aria-hidden="true">
      <path d="M0 14 Q0 4 14 4 L289 4 L289 44 L0 44 Z" fill="#1f2fb8"/>
      <path d="M0 30 Q140 18 289 26 L289 44 L0 44 Z" fill="#15208f" opacity="0.5"/>
    </svg>
  </main>
</body>
</html>
```